I need a website built for my organization.
We are the world's largest network of music producers.
The website should be professional, sharp, and high quality., We need a website built for The Harbor Sound Guild. We are one of the World's largest association of music producers.
The site must be professional, sharp, and high quality., I need a website built for my organization.
The site must be professional, sharp, and high quality.
Somewhere in the top half of the site there should be a form for the user to fill out. The details of the form are as follows:
Title (large and bold): Contact Us or Submit Your Music
Fields to include (* = required): First Name*, Last Name*, Age, Zip Code, Email Address*, Daytime Phone, Evening Phone, Comments
Then, there will be a "submit" button to proceed to next step of form. Just below the "submit" button, should be the following verbiage: "After submitting, you will have the opportunity to upload demos of your music (optional) and provide other pertinent information about yourself, band, or group."
Target Market(s)
Music producers and aspiring musicians
Industry/Entity Type
Group
Colors
Designer to choose colors to be used in the design.
Look and feel
Each slider illustrates characteristics of the customer's brand and the style your logo design should communicate.

```html
<!DOCTYPE html>
<html lang="en">
<head>
<meta charset="utf-8">
<title>The Harbor Sound Guild</title>
<link href="https://fonts.googleapis.com/css2?family=Raleway:ital,wght@0,400;0,500;0,600;0,700;0,800;1,400;1,500&display=swap" rel="stylesheet">
<style>
  :root {
    --ink: #22302f;
    --ink-soft: #7a8584;
    --orange: #fd6a21;
    --orange-ring: #ffd3bd;
    --rule: #e8e8e8;
    --grey-text: #b9b9b9;
    --btn-ring: #f4f4f4;
    --btn-glyph: #c4c4c4;
    --social-sky: #7dd3f5;
    --social-navy: #4a609c;
    --white: #ffffff;
  }
  * { box-sizing: border-box; margin: 0; padding: 0; }
  html, body { width: 989px; height: 1200px; overflow: hidden; background: var(--white); }
  body { font-family: "Raleway", sans-serif; color: var(--ink); padding-top: 32px; }

  .page { width: 756px; margin-left: 154px; }

  .site-header { height: 66px; display: flex; align-items: center; justify-content: space-between; }
  .brand-name { font-size: 36px; font-weight: 800; color: var(--ink); letter-spacing: -0.5px; }
  .social { display: flex; gap: 14px; }
  .social-link { width: 56px; height: 56px; border-radius: 50%; }
  .social-link.sky { background: var(--social-sky); }
  .social-link.navy { background: var(--social-navy); }
  .header-rule { margin-top: 20px; height: 2px; background: var(--rule); }

  .main-nav { list-style: none; margin: 18px 0 0 192px; }
  .main-nav li { display: flex; align-items: center; height: 44px; font-size: 22px; font-weight: 600; color: var(--ink); }
  .main-nav li.active { color: var(--orange); }
  .main-nav svg { width: 26px; height: 26px; margin-right: 28px; flex: none; }

  .submit-form { margin-top: 18px; }
  .form-title { font-size: 28px; line-height: 34px; font-weight: 800; color: var(--ink); margin-bottom: 10px; }
  .field-grid { display: grid; grid-template-columns: 1fr 1fr; column-gap: 24px; row-gap: 8px; }
  .field label { display: block; font-size: 14px; line-height: 18px; font-weight: 600; color: var(--ink); margin-bottom: 4px; }
  .field label em { font-style: normal; color: var(--orange); }
  .field input, .field textarea { display: block; width: 100%; height: 32px; border: 2px solid var(--rule); border-radius: 16px; padding: 0 14px; font-family: "Raleway", sans-serif; font-size: 15px; color: var(--ink); background: var(--white); }
  .field.comments { margin-top: 8px; }
  .field textarea { height: 44px; resize: none; padding: 10px 14px; }
  .submit-button { margin-top: 12px; height: 40px; padding: 0 40px; border: none; border-radius: 20px; background: var(--orange); color: var(--white); font-family: "Raleway", sans-serif; font-size: 18px; font-weight: 700; }
  .form-note { margin-top: 8px; font-size: 14px; line-height: 18px; color: var(--ink-soft); }

  .search-bar { margin-top: 22px; height: 64px; border-radius: 32px; background: var(--orange); box-shadow: 0 0 0 4px var(--orange-ring); display: flex; align-items: center; padding: 0 32px 0 36px; }
  .search-bar span { flex: 1; color: var(--white); font-size: 22px; font-style: italic; font-weight: 500; }
  .search-bar svg { width: 32px; height: 32px; }

  .player { margin-top: 26px; height: 96px; display: flex; align-items: center; }
  .player-button { border-radius: 50%; background: linear-gradient(#f2f2f2, #e2e2e2); box-shadow: 0 0 0 5px var(--btn-ring), 0 3px 4px rgba(0,0,0,0.08); display: flex; align-items: center; justify-content: center; flex: none; }
  .player-button.small { width: 70px; height: 70px; }
  .player-button.play { width: 92px; height: 92px; margin: 0 18px; }
  .volume-wrap { margin-left: auto; display: flex; align-items: center; gap: 8px; }
  .volume { position: relative; width: 200px; height: 18px; border-radius: 9px; background: var(--ink); }
  .volume-level { position: absolute; left: 3px; top: 3px; width: 140px; height: 12px; border-radius: 6px; background: var(--white); }
  .volume-icon { width: 18px; height: 26px; }

  .progress { position: relative; margin-top: 30px; height: 3px; background: var(--rule); }
  .progress-done { position: absolute; left: 0; top: 0; width: 175px; height: 3px; background: var(--orange); }
  .progress-knob { position: absolute; left: 163px; top: -11px; width: 25px; height: 25px; border-radius: 50%; background: var(--orange); }

  .track-row { margin-top: 26px; display: flex; justify-content: space-between; align-items: baseline; }
  .track-title { font-size: 26px; font-weight: 500; color: var(--orange); }
  .track-time { font-size: 22px; font-style: italic; color: var(--grey-text); }
</style>
</head>
<body>
<div class="page">
  <header class="site-header">
    <div class="brand-name">The Harbor Sound Guild</div>
    <div class="social">
      <a class="social-link sky" aria-label="Social profile"></a>
      <a class="social-link navy" aria-label="Social profile"></a>
    </div>
  </header>
  <div class="header-rule"></div>

  <ul class="main-nav">
    <li class="active">
      <svg viewBox="0 0 32 32"><path fill="#fd6a21" d="M16 4 2 16h4v12h8v-8h4v8h8V16h4z"/></svg>Welcome
    </li>
    <li>
      <svg viewBox="0 0 32 32"><g fill="#22302f"><circle cx="21" cy="10" r="5"/><path d="M11 28c0-7 4-10 10-10s10 3 10 10z"/><circle cx="10" cy="12" r="4" fill="#7a8584"/><path d="M1 26c0-6 3-8 9-8 2 0 3 0 4 1-3 2-4 4-4 7z" fill="#7a8584"/></g></svg>People
    </li>
    <li>
      <svg viewBox="0 0 32 32"><g fill="#22302f"><path d="M11 5h17v18h-3V9H14v16h-3z"/><ellipse cx="8" cy="25" rx="5" ry="4"/><ellipse cx="23" cy="23" rx="5" ry="4"/></g></svg>Music
    </li>
    <li>
      <svg viewBox="0 0 32 32"><path fill="#22302f" d="M16 2l4.2 9.3 10.1 1-7.6 6.8 2.2 10L16 24l-8.9 5.1 2.2-10-7.6-6.8 10.1-1z"/></svg>Favourites
    </li>
    <li>
      <svg viewBox="0 0 32 32"><g fill="none" stroke="#22302f" stroke-width="2"><rect x="6" y="3" width="20" height="26"/><path d="M11 3v26M21 3v26M6 10h5M6 16h5M6 22h5M21 10h5M21 16h5M21 22h5"/></g></svg>Videos
    </li>
  </ul>

  <form class="submit-form">
    <h2 class="form-title">Submit Your Music</h2>
    <div class="field-grid">
      <div class="field"><label for="first-name">First Name <em>*</em></label><input id="first-name" type="text" required></div>
      <div class="field"><label for="last-name">Last Name <em>*</em></label><input id="last-name" type="text" required></div>
      <div class="field"><label for="age">Age</label><input id="age" type="text"></div>
      <div class="field"><label for="zip">Zip Code</label><input id="zip" type="text"></div>
      <div class="field"><label for="email">Email Address <em>*</em></label><input id="email" type="email" required></div>
      <div class="field"><label for="day-phone">Daytime Phone</label><input id="day-phone" type="tel"></div>
      <div class="field"><label for="eve-phone">Evening Phone</label><input id="eve-phone" type="tel"></div>
    </div>
    <div class="field comments"><label for="comments">Comments</label><textarea id="comments"></textarea></div>
    <button class="submit-button" type="submit">Submit</button>
    <p class="form-note">After submitting, you will have the opportunity to upload demos of your music (optional) and provide other pertinent information about yourself, band, or group.</p>
  </form>

  <div class="search-bar" role="search">
    <span>Search for an artist, song...</span>
    <svg viewBox="0 0 42 42"><circle cx="17" cy="17" r="12" fill="none" stroke="#fff" stroke-width="4"/><path d="M26 26l11 11" stroke="#fff" stroke-width="4" stroke-linecap="round"/></svg>
  </div>

  <div class="player">
    <div class="player-button small" aria-label="Rewind">
      <svg width="30" height="19" viewBox="0 0 38 24"><path fill="#c4c4c4" d="M19 0v24L1 12zM37 0v24L19 12z"/></svg>
    </div>
    <div class="player-button play" aria-label="Play">
      <svg width="26" height="32" viewBox="0 0 34 42"><path fill="#c4c4c4" d="M2 0l32 21L2 42z"/></svg>
    </div>
    <div class="player-button small" aria-label="Fast forward">
      <svg width="30" height="19" viewBox="0 0 38 24"><path fill="#c4c4c4" d="M1 0v24l18-12zM19 0v24l18-12z"/></svg>
    </div>
    <div class="volume-wrap">
      <div class="volume" aria-label="Volume"><div class="volume-level"></div></div>
      <svg class="volume-icon" viewBox="0 0 22 32"><g fill="none" stroke="#22302f" stroke-width="2.5" stroke-linecap="round"><path d="M3 11a7 7 0 0 1 0 10"/><path d="M9 7a13 13 0 0 1 0 18"/><path d="M15 3a19 19 0 0 1 0 26"/></g></svg>
    </div>
  </div>

  <div class="progress" aria-label="Track progress">
    <div class="progress-done"></div>
    <div class="progress-knob"></div>
  </div>

  <div class="track-row">
    <div class="track-title">Marla Quinlan - Track 4</div>
    <div class="track-time">1.24/4.53</div>
  </div>
</div>
</body>
</html>
```